Business Card Design Project

i need a bussines car design
Veltra Clinical Hypnotherapy

Gordon Wexley
Psychotherapy & Hypnosis

64029381 /0427956120

back of the card appoinment space.

file was provided on a PDF, LOgo , use the blu colorsa as well , elegant, clear,

Target Market(s)

young professional, caucasian , young mothers.

Industry/Entity Type

Business

```html
<!DOCTYPE html>
<html lang="en">
<head>
<meta charset="utf-8">
<title>Veltra Hypnotherapy – Business Card</title>
<link rel="stylesheet" href="https://fonts.googleapis.com/css2?family=Questrial&display=swap">
<style>
  :root {
    --stage: #3b3b3b;
    --card: #ffffff;
    --blue: #2a7cc0;
    --blue-soft: #8dbde4;
    --ink: #2b2b2b;
    --muted: #555555;
    --photo-top: #e9e2d8;
    --photo-bottom: #d9cbb8;
    --badge: #9cbf3b;
  }
  * { box-sizing: border-box; margin: 0; padding: 0; }
  html, body { width: 1200px; height: 900px; overflow: hidden; }
  body {
    background: var(--stage);
    font-family: "Questrial", "Century Gothic", sans-serif;
    color: var(--ink);
    position: relative;
  }
  .card {
    position: absolute;
    top: 311px;
    width: 531px;
    height: 306px;
    background: var(--card);
    border-radius: 18px;
    overflow: hidden;
    box-shadow: 0 6px 14px rgba(0,0,0,.45);
  }
  .card--front { left: 74px; }
  .card--back { left: 636px; }

  .brand { position: absolute; display: flex; align-items: center; gap: 12px; }
  .brand__dot { width: 34px; height: 34px; border-radius: 50%; background: var(--blue); flex: none; }
  .brand__text { display: flex; flex-direction: column; }
  .brand__name { font-size: 23px; color: var(--blue); line-height: 1; letter-spacing: .2px; }
  .brand__url {
    margin-top: 4px; padding-top: 3px;
    border-top: 1px solid var(--blue);
    font-size: 10px; letter-spacing: 1.1px; color: var(--muted);
  }
  .card--front .brand { left: 30px; top: 42px; }
  .card--back .brand { left: 44px; top: 24px; }

  .photo {
    position: absolute; left: 335px; top: 22px; width: 190px; height: 284px;
    background: linear-gradient(180deg, var(--photo-top), var(--photo-bottom));
  }

  .person { position: absolute; left: 29px; top: 142px; }
  .person__name { font-size: 23px; color: var(--blue); line-height: 1.1; letter-spacing: .3px; }
  .person__role { font-size: 15px; color: var(--ink); margin-top: 4px; }

  .badge {
    position: absolute; left: 278px; top: 148px; width: 40px; height: 40px;
    border-radius: 50%; background: var(--badge); border: 2px solid #d8d8d8;
  }

  .contacts { position: absolute; left: 30px; top: 213px; list-style: none; }
  .contacts li { display: flex; align-items: center; gap: 6px; font-size: 12.5px; color: var(--ink); height: 17px; }
  .contacts svg { width: 10px; height: 10px; fill: var(--blue); flex: none; }

  .appointments { position: absolute; left: 44px; top: 80px; list-style: none; }
  .appointments li { display: flex; align-items: flex-end; font-size: 16px; line-height: 1; color: var(--ink); height: 28px; }
  .blank { display: inline-block; border-bottom: 1px solid var(--ink); height: 1px; margin-bottom: 2px; }
  .blank--time { width: 32px; margin-left: 6px; }
  .blank--name { width: 140px; margin: 0 5px 2px 6px; }
  .blank--day { width: 22px; }
  .blank--month { width: 30px; }
  .blank--year { width: 36px; }
  .sep { margin: 0 1px; }

  .notice { position: absolute; left: 44px; top: 238px; font-size: 10.5px; color: var(--muted); line-height: 1.2; }
  .registration { position: absolute; left: 44px; top: 264px; font-size: 12px; color: var(--muted); }
</style>
</head>
<body>

<section class="card card--front">
  <div class="brand">
    <span class="brand__dot"></span>
    <div class="brand__text">
      <span class="brand__name">Veltra Hypnotherapy</span>
      <span class="brand__url">www.veltraclinicalhypnotherapy.com.au</span>
    </div>
  </div>

  <div class="person">
    <div class="person__name">Gordon Wexley</div>
    <div class="person__role">Psychotherapy &amp; Hypnosis</div>
  </div>

  <span class="badge" aria-hidden="true"></span>

  <ul class="contacts">
    <li><svg viewBox="0 0 10 10"><path d="M5 0a3.5 3.5 0 0 0-3.5 3.5C1.5 6 5 10 5 10s3.5-4 3.5-6.5A3.5 3.5 0 0 0 5 0zm0 5a1.4 1.4 0 1 1 0-2.8A1.4 1.4 0 0 1 5 5z"/></svg>148 Halden Street, Kingsmere 3021</li>
    <li><svg viewBox="0 0 10 10"><path d="M2 0.5l2 2-1 1.3c.6 1.3 1.6 2.3 2.9 2.9L7.2 5.7l2 2-1.3 1.8C4.3 9.3.7 5.7.3 2.1z"/></svg>0427 956 120</li>
    <li><svg viewBox="0 0 10 10"><path d="M2.5 0h5a1 1 0 0 1 1 1v8a1 1 0 0 1-1 1h-5a1 1 0 0 1-1-1V1a1 1 0 0 1 1-1zm0 1.2v6.6h5V1.2z"/></svg>6402 9381</li>
    <li><svg viewBox="0 0 10 10"><path d="M0 2h10v.6L5 5.6 0 2.6zm0 1.8l5 3 5-3V8H0z"/></svg>gordon@veltraclinicalhypnotherapy.com.au</li>
  </ul>

  <div class="photo" role="img" aria-label="Portrait photograph of the therapist, arms folded, in a light shirt"></div>
</section>

<section class="card card--back">
  <div class="brand">
    <span class="brand__dot"></span>
    <div class="brand__text">
      <span class="brand__name">Veltra Hypnotherapy</span>
      <span class="brand__url">www.veltraclinicalhypnotherapy.com.au</span>
    </div>
  </div>

  <ol class="appointments">
    <li>1.<span class="blank blank--time"></span>am/pm<span class="blank blank--name"></span><span class="blank blank--day"></span><span class="sep">/</span><span class="blank blank--month"></span><span class="sep">/</span><span class="blank blank--year"></span></li>
    <li>2.<span class="blank blank--time"></span>am/pm<span class="blank blank--name"></span><span class="blank blank--day"></span><span class="sep">/</span><span class="blank blank--month"></span><span class="sep">/</span><span class="blank blank--year"></span></li>
    <li>3.<span class="blank blank--time"></span>am/pm<span class="blank blank--name"></span><span class="blank blank--day"></span><span class="sep">/</span><span class="blank blank--month"></span><span class="sep">/</span><span class="blank blank--year"></span></li>
    <li>4.<span class="blank blank--time"></span>am/pm<span class="blank blank--name"></span><span class="blank blank--day"></span><span class="sep">/</span><span class="blank blank--month"></span><span class="sep">/</span><span class="blank blank--year"></span></li>
    <li>5.<span class="blank blank--time"></span>am/pm<span class="blank blank--name"></span><span class="blank blank--day"></span><span class="sep">/</span><span class="blank blank--month"></span><span class="sep">/</span><span class="blank blank--year"></span></li>
  </ol>

  <p class="notice">To reschedule your appointment, please SMS or phone 0427 956 120<br>at least 24 hours prior to your allocated time. Thank you.</p>
  <p class="registration">CHPB Registration No. NPM058214</p>
</section>

</body>
</html>
```